need corporate, modern business card created for Consulting Company

I need a slick business card using elements from my website, as well as, integrating my pixelforge-created logo (see files).

The business card needs to be:
1. Corporate and modern
2. Clean and professional

I've included a PSD with the logo/icon that you can use to create it. Feel free to try a metallic finish on the logo, make it bigger/small, underlay it. Whatever you need to do to make my card stand out.

Try a black background, or white background or gray.

The idea is for my card to be memorable as well as professional and corporate.

Target Market(s)

Corporate business in the US and Canada.

Industry/Entity Type

Business

Contact Information for Business Card

Enterprise Advancing Solutions
Martin Coble, Senior Partner
office: 1 877 555 0143
mobile: 1 519 555 0172
website: http://www.velmorant.com

Requirements
Must have
• Card-related information
• corporate, yet modern
• clean and professional
• incorporate the icon only
• must have an editable form when complete!
Nice to have
• metallic icon might be cool
• try it with white or black

```html
<!DOCTYPE html>
<html lang="en">
<head>
<meta charset="utf-8">
<title>Enterprise Advancing Solutions – Business Card</title>
<link rel="stylesheet" href="https://fonts.googleapis.com/css2?family=Ubuntu:wght@400;500;700&display=swap">
<style>
  :root {
    --stage: #141414;
    --card-black: #0b0b0b;
    --card-white: #ffffff;
    --silver: #c8c8c8;
    --ink: #1c1c1c;
    --ink-soft: #3a3a3a;
    --icon-grey: #4d4d4d;
  }
  * { margin: 0; padding: 0; box-sizing: border-box; }
  html, body {
    width: 1200px; height: 1000px; overflow: hidden;
    background: var(--stage);
    font-family: "Ubuntu", sans-serif;
  }
  .stage { position: relative; width: 1200px; height: 1000px; }

  .card {
    position: absolute; left: 320px; width: 560px; height: 320px;
    box-shadow: 0 18px 40px rgba(0,0,0,.6);
  }

  /* front */
  .card-front {
    top: 140px; background: var(--card-black);
    display: flex; align-items: center; justify-content: center;
  }
  .wordmark { display: flex; align-items: center; gap: 18px; color: var(--silver); font-weight: 500; }
  .wordmark-square { width: 34px; height: 34px; background: var(--silver); border-radius: 4px; }
  .wordmark-text { display: flex; flex-direction: column; }
  .wordmark-name { font-size: 42px; letter-spacing: 1px; line-height: 1; }
  .wordmark-tag { font-size: 15px; letter-spacing: 7px; margin-top: 8px; }

  /* back */
  .card-back { top: 540px; background: var(--card-white); overflow: hidden; }
  .edge-tab { position: absolute; left: 0; top: 130px; width: 8px; height: 26px; background: var(--ink); }
  .contact { position: absolute; left: 52px; top: 120px; color: var(--ink); }
  .contact-name { font-size: 21px; font-weight: 700; letter-spacing: .5px; }
  .contact-role { font-size: 14px; color: var(--ink-soft); margin-top: 2px; }
  .contact-lines { list-style: none; margin-top: 30px; font-size: 15px; line-height: 25px; color: var(--ink); }
  .icon-field {
    position: absolute; right: 0; top: 0; width: 48%; height: 100%;
    background: linear-gradient(115deg, rgba(77,77,77,0) 0%, rgba(77,77,77,.55) 45%, var(--icon-grey) 100%);
  }
</style>
</head>
<body>
<main class="stage">
  <section class="card card-front">
    <div class="wordmark">
      <span class="wordmark-square"></span>
      <div class="wordmark-text">
        <span class="wordmark-name">ADVANCING</span>
        <span class="wordmark-tag">SOLUTIONS</span>
      </div>
    </div>
  </section>

  <section class="card card-back">
    <span class="edge-tab"></span>
    <div class="contact">
      <h1 class="contact-name">MARTIN COBLE</h1>
      <p class="contact-role">Senior Partner</p>
      <ul class="contact-lines">
        <li>o : 1 877 555 0143</li>
        <li>m : 1 519 555 0172</li>
        <li>w : www.velmorant.com</li>
      </ul>
    </div>
    <div class="icon-field" role="img" aria-label="Large grey brand icon decoration"></div>
  </section>
</main>
</body>
</html>
```